Brightpath Dentistry - Flyer - Modern & Eye catching campaign flyer

Need front & back side full page flyer designs for both 1) Grand opening 2) On-going campaign.

Attached the new dental office logo.
Attached our other dental clinic flyer designs for content.

Target Market(s)

Cosmetic dentistry

Industry/Entity Type

Health Care

Requirements
Must have
• decent, modern and eye catching marketing flyers.
Nice to have
• - Nice space
• - Highlight phone number
• - Highlight special features like convenient hours, call or text, for all ages, digital facility, etc
Should not have
• - Don't want to fill the flyer with too much wordings
• - Too many colors

```html
<!DOCTYPE html>
<html lang="en">
<head>
<meta charset="utf-8">
<title>Brightpath Dentistry – Flyers</title>
<link href="https://fonts.googleapis.com/css2?family=Titillium+Web:wght@600;700;900&family=Open+Sans:wght@400;600;700&display=swap" rel="stylesheet">
<style>
  :root{
    --bg:#d3d3d3;
    --navy:#1f4e87;
    --blue:#3473bd;
    --deep:#1b3a6b;
    --sky:#a3ddf0;
    --ice:#e3f3fa;
    --cyan:#1aa6d6;
    --orange:#f15a1f;
    --ink:#1d1d1d;
    --white:#ffffff;
  }
  *{margin:0;padding:0;box-sizing:border-box}
  html,body{width:1200px;height:799px;overflow:hidden}
  body{background:var(--bg);position:relative;font-family:"Open Sans",sans-serif}
  .flyer{position:absolute;top:86px;width:446px;height:626px;overflow:hidden;box-shadow:0 6px 18px rgba(0,0,0,.25)}
  .flyer--front{left:115px}
  .flyer--back{left:639px}
  .flyer__bg{position:absolute;inset:0;width:100%;height:100%}
  .abs{position:absolute}
  .head{font-family:"Titillium Web",sans-serif;font-weight:700}
  .brand{font-family:"Titillium Web",sans-serif;font-weight:700;color:var(--cyan);white-space:nowrap;line-height:1}
  .photo{position:absolute;border-radius:50%;border:5px solid #8c9aa8;box-shadow:0 4px 10px rgba(0,0,0,.3)}
  .badge{position:absolute;border-radius:50%;background:radial-gradient(circle at 50% 40%,#ffffff,var(--ice) 70%,#cde7f2);border:3px solid var(--navy);box-shadow:0 4px 12px rgba(0,0,0,.35);text-align:center;display:flex;flex-direction:column;justify-content:center;align-items:center;color:var(--navy)}
  .call__title{font-family:"Titillium Web",sans-serif;font-weight:700;line-height:1}
  .call__sub{font-family:"Titillium Web",sans-serif;font-weight:700;line-height:1.2}
  .call__phone{font-family:"Titillium Web",sans-serif;font-weight:700;color:var(--orange);line-height:1.2}
  .pill{position:absolute;background:var(--white);border:2px solid var(--orange);border-radius:20px;display:flex;align-items:center;justify-content:center;box-shadow:0 3px 6px rgba(0,0,0,.25);white-space:nowrap}

  /* front */
  .headline{position:absolute;left:0;width:266px;text-align:center;color:var(--navy);line-height:1;font-family:"Titillium Web",sans-serif;font-weight:900}
  .headline--grand{top:136px;font-size:50px}
  .headline--opening{top:186px;font-size:50px}
  .headline--specials{top:234px;font-size:36px;color:var(--orange)}
  .specials{position:absolute;left:22px;top:288px;width:217px;height:83px;background:var(--white);border:2px solid var(--orange);border-radius:12px;box-shadow:0 3px 8px rgba(0,0,0,.25);padding:9px 0 0 14px;list-style:none}
  .specials li{font-family:"Titillium Web",sans-serif;font-weight:600;color:var(--orange);font-size:14.5px;line-height:19px;white-space:nowrap}
  .specials li::before{content:"";display:inline-block;width:8px;height:8px;border-radius:50%;background:var(--orange);margin-right:8px;vertical-align:2px}
  .service{position:absolute;display:flex;align-items:center;gap:5px;color:var(--white);font-family:"Titillium Web",sans-serif;font-weight:700;font-size:9.2px;line-height:1.15;white-space:nowrap}
  .service__icon{width:18px;height:18px;border:2px solid var(--white);border-radius:50%;flex:none}
  .service--stack{flex-direction:column;text-align:center;gap:3px}

  /* back */
  .tagline{position:absolute;left:160px;width:256px;text-align:center;color:var(--orange);font-family:"Titillium Web",sans-serif;font-weight:700;font-size:20px;line-height:25px}
  .copy{position:absolute;color:var(--ink);font-size:8.3px;line-height:12.6px}
  .question{position:absolute;left:57px;top:304px;color:var(--orange);font-family:"Titillium Web",sans-serif;font-weight:700;line-height:1;white-space:nowrap}
  .map{position:absolute;left:29px;top:463px;width:185px;height:102px;border:2px solid var(--orange);border-radius:14px;background:linear-gradient(135deg,#eef0f2,#dfe3e8);box-shadow:0 3px 6px rgba(0,0,0,.25)}
</style>
</head>
<body>

<!-- Front: grand opening -->
<section class="flyer flyer--front">
  <svg class="flyer__bg" viewBox="0 0 446 626" preserveAspectRatio="none" aria-hidden="true">
    <defs>
      <linearGradient id="frontBase" x1="0" y1="0" x2="1" y2="1">
        <stop offset="0" stop-color="#2d66ad"/>
        <stop offset="1" stop-color="#3d83c9"/>
      </linearGradient>
      <linearGradient id="frontSwoosh" x1="0" y1="0" x2="0" y2="1">
        <stop offset="0" stop-color="#ffffff"/>
        <stop offset=".45" stop-color="#d6d6d6"/>
        <stop offset=".75" stop-color="#ffffff"/>
      </linearGradient>
    </defs>
    <rect width="446" height="626" fill="url(#frontBase)"/>
    <path d="M0,140 C150,105 250,25 330,0 L446,0 L446,70 C330,95 180,175 0,240 Z" fill="var(--sky)"/>
    <path d="M0,175 C160,135 300,55 446,22 L446,212 C330,245 255,315 205,360 C150,405 60,405 0,412 Z" fill="url(#frontSwoosh)"/>
    <path d="M0,412 C60,405 150,405 205,360 C255,315 330,245 446,212 L446,238 C335,270 265,340 215,392 C160,445 60,455 0,470 Z" fill="var(--sky)"/>
    <path d="M0,470 C60,455 160,445 215,392 C240,368 260,350 280,336 C250,380 200,440 140,470 C90,495 40,498 0,500 Z" fill="#7ec8e6" opacity=".6"/>
  </svg>

  <div class="abs brand" style="left:28px;top:96px;font-size:22px">Brightpath Dentistry</div>

  <div class="headline headline--grand">GRAND</div>
  <div class="headline headline--opening">OPENING</div>
  <div class="headline headline--specials">SPECIALS</div>

  <div class="photo" role="img" aria-label="Photo of a smiling young woman holding a clear aligner" style="left:246px;top:35px;width:176px;height:176px;background:radial-gradient(circle at 50% 40%,#f3e1d3,#d8b89c 55%,#e9e9e9 80%)"></div>

  <ul class="specials">
    <li>Free Kids Dental Screening</li>
    <li>$25 Adults Dental Screening</li>
    <li>15% off on Treatment Plan</li>
  </ul>

  <div class="badge" style="left:295px;top:230px;width:130px;height:130px">
    <div class="call__title" style="font-size:23px">CALL</div>
    <div class="call__sub" style="font-size:11px;margin-top:3px">OR TEXT US NOW:</div>
    <div class="call__phone" style="font-size:15.5px">555.204.7381</div>
  </div>

  <div class="service" style="left:280px;top:375px"><span class="service__icon"></span>GLOW TEETH WHITENING</div>
  <div class="service" style="left:198px;top:408px"><span class="service__icon"></span>ROOT CANAL THERAPY</div>
  <div class="service" style="left:335px;top:426px"><span class="service__icon"></span>NIGHT GUARDS</div>
  <div class="service" style="left:155px;top:444px"><span class="service__icon"></span>IMPLANTS</div>
  <div class="service" style="left:260px;top:452px"><span class="service__icon"></span>EXTRACTIONS</div>
  <div class="service" style="left:133px;top:488px"><span class="service__icon"></span>VENEERS</div>
  <div class="service" style="left:246px;top:495px"><span class="service__icon"></span>DENTURES</div>
  <div class="service service--stack" style="left:338px;top:483px"><span class="service__icon"></span>CLEAR ALIGNERS<br>(Invisible braces)</div>
  <div class="service" style="left:27px;top:511px"><span class="service__icon"></span>CROWN AND<br>BRIDGE</div>

  <div class="pill" style="left:143px;top:535px;width:160px;height:28px">
    <span class="head" style="color:var(--navy);font-size:14px">www.BrightpathSmiles.com</span>
  </div>
  <div class="pill" style="left:37px;top:566px;width:372px;height:34px">
    <span class="head" style="color:var(--orange);font-size:16.5px">CONVENIENT EVENING &amp; SATURDAY HOURS</span>
  </div>
</section>

<!-- Back: ongoing campaign -->
<section class="flyer flyer--back">
  <svg class="flyer__bg" viewBox="0 0 446 626" preserveAspectRatio="none" aria-hidden="true">
    <defs>
      <linearGradient id="backBase" x1="0" y1="0" x2="1" y2="0">
        <stop offset="0" stop-color="#3470b5"/>
        <stop offset="1" stop-color="#1b3a6b"/>
      </linearGradient>
      <linearGradient id="backFoot" x1="0" y1="0" x2="1" y2="1">
        <stop offset="0" stop-color="#4aa3c2"/>
        <stop offset="1" stop-color="#a7dcec"/>
      </linearGradient>
    </defs>
    <rect width="446" height="626" fill="url(#backBase)"/>
    <path d="M0,170 C100,150 165,45 270,12 C345,-8 385,80 446,110 L446,626 L0,626 Z" fill="var(--sky)"/>
    <path d="M0,215 C110,195 185,95 285,62 C345,45 390,125 446,165 L446,330 C390,300 330,360 290,420 C250,470 200,470 150,478 C90,488 40,468 0,425 Z" fill="var(--white)"/>
    <path d="M446,330 C390,300 330,360 290,420 C330,380 390,360 446,390 Z" fill="var(--blue)"/>
    <path d="M0,425 C40,468 90,488 150,478 C110,500 60,505 0,480 Z" fill="var(--sky)"/>
    <path d="M0,480 C60,505 110,500 150,478 C120,530 60,560 0,560 Z" fill="var(--blue)"/>
    <path d="M0,560 C60,560 120,530 150,478 C200,470 250,470 290,420 C270,520 200,600 120,626 L0,626 Z" fill="url(#backFoot)"/>
  </svg>

  <div class="badge" style="left:34px;top:25px;width:106px;height:106px">
    <div class="call__title" style="font-size:20px">All</div>
    <div class="call__sub" style="font-size:13px;line-height:1.15">INSURANCES<br>ACCEPTED</div>
  </div>

  <div class="tagline" style="top:84px">FAMILY &amp; COSMETICS<br>DENTISTRY</div>

  <p class="copy" style="left:220px;top:142px;width:200px">State-Of-The-Art equipment and paperless facility. Filled with entertain-ment devices for patient comfort.<br>Same-day appointment for<br>DENTAL EMERGENCIES.<br>Helping community with routine<br>free kids dental screening.</p>

  <div class="abs brand" style="left:20px;top:244px;font-size:29px">Brightpath Dentistry</div>

  <div class="badge" style="left:311px;top:234px;width:110px;height:110px">
    <div class="call__title" style="font-size:18px">CALL</div>
    <div class="call__sub" style="font-size:9.5px;margin-top:2px">OR TEXT US NOW:</div>
    <div class="call__phone" style="font-size:13px">555.204.7381</div>
  </div>

  <div class="question" style="font-size:18px">LOOKING FOR DENTIST</div>
  <div class="question" style="top:326px;font-size:23px">CLOSE TO HOME?</div>

  <p class="copy" style="left:82px;top:356px;width:150px;font-size:8.6px">Come and See Us for Professional Services and Care. Our dentists and staff are experts in the field of advanced dentistry and will help you achive your perfect smile.</p>
  <p class="copy" style="left:90px;top:430px;width:130px;text-align:center;font-size:8.6px">Dr. Mira Hollis, D.D.S</p>

  <div class="map" role="img" aria-label="Street map showing the office location"></div>
  <div class="pill" style="left:31px;top:572px;width:182px;height:24px">
    <span style="font-weight:700;color:var(--ink);font-size:8.5px">412 Maple Crest Ave, Fairview PA 19000</span>
  </div>

  <div class="photo" role="img" aria-label="Photo of a smiling family of four together" style="left:233px;top:380px;width:194px;height:194px;background:radial-gradient(circle at 50% 45%,#f1dccb,#d9b395 50%,#eef0f2 80%)"></div>
</section>

</body>
</html>
```